Graphics Design of Physics Book

Hi
Size : 8" x 11.25"
We are education book Publication Company and would like to have book cover for "Physics" it has 4 volumes. All 4 having the same color scheme and design except the volume no.
Blue is my personal favorite but u can use any color. Want to have a band at the bottom of the cover to place our Logo “VARNEL Education” a PDF of the same is attached, or you can place logo anywhere according to ur design.
I need “Physics” as title of the book to be visible prominently.
And volume and volume no. should also be Visible and eye catching I prefer a Graphic to enhance the Volume No.
A background pattern can also be a option (it should be vector form so that color can be change later)
Please do not offer any cut and paste design I need very professional presentation.
Volume and Number can be in metallic 3D (CMYK) effect.
only Professional presentation will get feedback.
I have provided a sample artwork for reference do not follow it but can be a reference what I needed !

Target Market(s)

Students Class 9th to 12th

Industry/Entity Type

Education

Font styles to use
Serif

Colors
3176b5
0555a3
85abd2
cadf82
abd036
9bcb3c

Requirements
Must have
• Eye catching.
• “Physics” as title of the book to be visible prominently.
• volume and volume no. should also be Visible and eye catching
• I prefer a Graphic to enhance the Volume No.
• Icons for
• 1. Questions and answers
• 2. Theory Notes
• 3. Tips & Tricks
• 4. Previous Year's Reference Questions
• 5. Covers Complete Syllabus
Nice to have
• decent seamless background or metallic 3d effect (not to be print in special Ink) design should only be in CMYK.
Should not have
• Physics related Pictures or Icons (Specially E=mc2) or any scientist photograph or I Need pure graphic design

```html
<!DOCTYPE html>
<html lang="en">
<head>
<meta charset="utf-8">
<title>Physics – Volume 1</title>
<link rel="stylesheet" href="https://fonts.googleapis.com/css2?family=Arvo:ital,wght@0,700;1,700&family=Roboto+Condensed:ital,wght@0,700;1,400&display=swap">
<style>
  :root {
    --deep-blue: #0b5cb0;
    --mid-blue: #1d78c8;
    --sky: #57b8e8;
    --pale-sky: #9fd8f2;
    --ribbon: #1fb0df;
    --ribbon-shade: #1687b0;
    --title-outline: #3aa6de;
    --white: #ffffff;
    --ink: #111111;
  }
  html, body {
    margin: 0;
    padding: 0;
    overflow: hidden;
    background: #ffffff;
  }
  .cover {
    position: relative;
    width: 835px;
    height: 1200px;
    overflow: hidden;
  }
  .cover-art {
    position: absolute;
    inset: 0;
  }
  .title {
    font-family: "Arvo", Georgia, serif;
    font-style: italic;
    font-weight: 700;
  }
  .feature-label {
    font-family: "Roboto Condensed", "Arial Narrow", sans-serif;
    font-style: italic;
    font-weight: 400;
    font-size: 24px;
    fill: var(--white);
  }
  .publisher {
    position: absolute;
    left: 48px;
    top: 1090px;
    width: 212px;
    height: 62px;
    background: var(--white);
    border: 2px solid var(--ink);
    display: flex;
    flex-direction: column;
    align-items: center;
    justify-content: center;
    font-family: "Roboto Condensed", "Arial Narrow", sans-serif;
    font-weight: 700;
    color: var(--ink);
    line-height: 1;
  }
  .publisher-name { font-size: 34px; letter-spacing: 2px; }
  .publisher-line { font-size: 17px; letter-spacing: 3px; margin-top: 3px; }
  .volume-number {
    font-family: "Arvo", Georgia, serif;
    font-weight: 700;
    font-style: normal;
  }
</style>
</head>
<body>
<div class="cover">
  <svg class="cover-art" width="835" height="1200" viewBox="0 0 835 1200" xmlns="http://www.w3.org/2000/svg">
    <defs>
      <linearGradient id="skyTop" x1="0" y1="0" x2="0" y2="1">
        <stop offset="0" stop-color="#0a55a8"/>
        <stop offset="1" stop-color="#1a7bcc"/>
      </linearGradient>
      <linearGradient id="skyLow" x1="0" y1="0" x2="0" y2="1">
        <stop offset="0" stop-color="#6cc6ee"/>
        <stop offset="1" stop-color="#5ab7e6"/>
      </linearGradient>
      <linearGradient id="ribbonFace" x1="0" y1="0" x2="0" y2="1">
        <stop offset="0" stop-color="#2bbbe6"/>
        <stop offset="1" stop-color="#14a4d6"/>
      </linearGradient>
      <linearGradient id="bannerFace" x1="0" y1="0" x2="1" y2="0">
        <stop offset="0" stop-color="#2a8fd6"/>
        <stop offset="1" stop-color="#59b3ea"/>
      </linearGradient>
      <radialGradient id="silver" cx="0.4" cy="0.35" r="0.75">
        <stop offset="0" stop-color="#f4f4f4"/>
        <stop offset="0.55" stop-color="#b9bcc0"/>
        <stop offset="1" stop-color="#6f7378"/>
      </radialGradient>
      <linearGradient id="silverRim" x1="0" y1="0" x2="1" y2="1">
        <stop offset="0" stop-color="#ffffff"/>
        <stop offset="0.5" stop-color="#8e9297"/>
        <stop offset="1" stop-color="#e6e6e6"/>
      </linearGradient>
      <filter id="softShadow" x="-10%" y="-10%" width="120%" height="130%">
        <feDropShadow dx="3" dy="5" stdDeviation="4" flood-color="#06325f" flood-opacity="0.55"/>
      </filter>
    </defs>

    <!-- background -->
    <rect class="bg-top" width="835" height="1200" fill="url(#skyTop)"/>
    <circle cx="860" cy="210" r="300" fill="#2f8fda" opacity="0.55"/>
    <circle cx="900" cy="520" r="330" fill="#3c9fe0" opacity="0.45"/>
    <path d="M0 560 C 200 470 500 470 835 540 L 835 1200 L 0 1200 Z" fill="url(#skyLow)"/>
    <path d="M0 760 C 250 660 560 650 835 730 L 835 1200 L 0 1200 Z" fill="#7fcff2" opacity="0.55"/>
    <circle cx="900" cy="960" r="330" fill="#a8dcf5" opacity="0.45"/>
    <path d="M0 1095 L 835 1095 L 835 1112 L 0 1112 Z" fill="#b8e4f7" opacity="0.6"/>

    <!-- title banner -->
    <g class="title-banner" filter="url(#softShadow)">
      <polygon points="60,360 120,350 120,420 75,430" fill="#13609f"/>
      <polygon points="105,345 790,300 800,372 118,412" fill="url(#bannerFace)"/>
    </g>

    <!-- title -->
    <text class="title" x="52" y="312" font-size="178"
          textLength="740" lengthAdjust="spacingAndGlyphs"
          fill="var(--white)" stroke="var(--title-outline)" stroke-width="12"
          paint-order="stroke" stroke-linejoin="round" filter="url(#softShadow)">Physics</text>

    <!-- feature list -->
    <g class="features">
      <g transform="translate(0,615)">
        <polygon points="535,0 565,14 565,58 535,44" fill="var(--ribbon-shade)"/>
        <rect x="118" y="0" width="420" height="44" fill="url(#ribbonFace)"/>
        <text class="feature-label" x="128" y="31">QUESTIONS AND ANSWERS</text>
        <rect x="48" y="0" width="32" height="32" rx="6" fill="#8e3fb0"/>
        <text x="64" y="24" text-anchor="middle" font-family="Roboto Condensed, sans-serif" font-weight="700" font-size="22" fill="#fff">Q</text>
        <rect x="72" y="12" width="32" height="32" rx="6" fill="#f07a2a"/>
        <text x="88" y="36" text-anchor="middle" font-family="Roboto Condensed, sans-serif" font-weight="700" font-size="22" fill="#fff">A</text>
      </g>
      <g transform="translate(0,670)">
        <polygon points="535,0 565,14 565,58 535,44" fill="var(--ribbon-shade)"/>
        <rect x="118" y="0" width="420" height="44" fill="url(#ribbonFace)"/>
        <text class="feature-label" x="128" y="31">THEORY NOTES</text>
        <rect x="52" y="-4" width="48" height="48" rx="10" fill="#ffffff"/>
        <rect x="56" y="0" width="40" height="40" rx="8" fill="#1f3f6e"/>
        <path d="M64 33 L 68 25 L 84 8 L 88 12 L 72 29 Z" fill="#cfe3f5"/>
        <path d="M64 36 C 72 32 80 38 90 33" stroke="#cfe3f5" stroke-width="2" fill="none"/>
      </g>
      <g transform="translate(0,726)">
        <polygon points="535,0 565,14 565,58 535,44" fill="var(--ribbon-shade)"/>
        <rect x="118" y="0" width="420" height="44" fill="url(#ribbonFace)"/>
        <text class="feature-label" x="128" y="31">TIPS &amp; TRICKS</text>
        <rect x="52" y="-4" width="48" height="48" rx="10" fill="#ffffff"/>
        <rect x="56" y="0" width="40" height="40" rx="8" fill="#f5a623"/>
        <circle cx="76" cy="16" r="9" fill="#fff"/>
        <rect x="71" y="24" width="10" height="9" rx="2" fill="#fff"/>
      </g>
      <g transform="translate(0,781)">
        <polygon points="535,0 565,14 565,58 535,44" fill="var(--ribbon-shade)"/>
        <rect x="118" y="0" width="420" height="44" fill="url(#ribbonFace)"/>
        <text class="feature-label" x="128" y="31" textLength="396" lengthAdjust="spacingAndGlyphs">PREVIOUS YEAR'S REFERENCE QUESTIONS</text>
        <path d="M54 38 C 44 38 44 22 56 22 C 56 8 76 4 82 16 C 96 12 104 26 96 38 Z" fill="#f0652a"/>
        <circle cx="66" cy="27" r="7" fill="#fff"/>
        <circle cx="84" cy="29" r="7" fill="#fff"/>
      </g>
      <g transform="translate(0,836)">
        <polygon points="535,0 565,14 565,58 535,44" fill="var(--ribbon-shade)"/>
        <rect x="118" y="0" width="420" height="44" fill="url(#ribbonFace)"/>
        <text class="feature-label" x="128" y="31">COVERS COMPLETE SYLLABUS</text>
        <rect x="52" y="-4" width="48" height="48" rx="10" fill="#ffffff"/>
        <rect x="56" y="0" width="40" height="40" rx="8" fill="#2e9e4a"/>
        <rect x="64" y="5" width="24" height="31" rx="2" fill="#fff"/>
        <rect x="70" y="2" width="12" height="6" rx="2" fill="#1f6e33"/>
        <path d="M68 15 H84 M68 21 H84 M68 27 H84" stroke="#2e9e4a" stroke-width="2"/>
      </g>
      <polygon points="535,880 565,894 565,912 535,912" fill="var(--ribbon-shade)"/>
    </g>

    <!-- volume medallion -->
    <g class="volume-badge">
      <circle cx="736" cy="1100" r="98" fill="var(--white)"/>
      <circle cx="736" cy="1100" r="85" fill="url(#silverRim)"/>
      <circle cx="736" cy="1100" r="73" fill="url(#silver)"/>
      <text class="volume-number" x="736" y="1140" text-anchor="middle" font-size="110"
            fill="#4a4e53" stroke="#e9e9e9" stroke-width="3" paint-order="stroke">1</text>
    </g>
  </svg>

  <div class="publisher">
    <span class="publisher-name">VARNEL</span>
    <span class="publisher-line">EDUCATION</span>
  </div>
</div>
</body>
</html>
```